Smart, intuitive SaaS software dashboard design

PactBloom is an innovative modern SaaS (software as a service) solution for contract and meeting management.

What we are looking for is fresh ideas for our dashboard. We do not need web coding or actionable wireframes now – but purely great design ideas from where to continue forward.

How should a modern web software dashboard look like? Fresh, intuitive, easy-to-use, and adaptable for responsive mobile designs. We hope that when the user logs into the service and sees the dashboard, he/she gets a good big picture of the current status of the most important documents of his/hers company.

To get to know the service and see the components, we kindly ask you to register to our service at www.pactbloom-demo.net and to utilize the free trial (30 days) so you can see the existing dashboard live. And also try out how it works. Might help you to get ideas how to improve it.

(The designer we will choose might be offered later on to design some other pages as well (contract view and edit pages, meeting page etc).)

You’ll find additional information in the attachment.

You’ll find more information of the company and the service also at www.pactbloom-demo.net

Target Market(s)

Global

Industry/Entity Type

Business Management

Number of Pages Required

1 page

Font styles to use
Sans Serif

Requirements
Must have
• 1) Clear design idea for us to iterate from, 2) Modern look and feel - elegant & bold at the same time - still with credibility in our target group. And 3) Suitable for dashboard usage - it should it a clear big picture for the user.
• UPDATE:
• Users should see most important things with one glance. Therefore we would like to see AT LEAST these items mentioned below on the first page.
• NOTE: if all these things are visible on the dashboard, the menu list is maybe not needed on the left. (And there might be some icons on the top header with needed settings/inbox features anyway.)
• NOTE2: as explained earlier, the design should be responsive i.e. work without modifications in PC, iPad and mobile (the areas/boxes would just rearrange themselves on top of each other.)
• -First area should be Documents, which would include different document categories: Contracts, Finance & Admin and HR
• -All different types of Meetings could be the next area (upcoming ones clearly visible with date and maybe description, time and location visible also).
• -Reminders and Activity Feed (they might also be together in top of each other, so that Reminder is visible first and Activity feed can be chosen from the tab.)
• -Virtual Datarooms (maybe 1-3 different ones with some analytics for each visible e.g. like usage/visits per day)
• Saved searches in very important list as users can save their most important searches. There are typically many of these, so at least 5 should be visible and then see all button (maybe even more could be visible if they fit on your design)
• My Latest is also important.
• (As explained, Action Required area is NOT needed anymore).
Nice to have
• Surprise us!
Should not have
• Please avoid the boring traditional legacy stuff and the common report dashboards.
• You do not need design a 100% mockup for the techie to continue with. The ideas count.

```html
<!DOCTYPE html>
<html lang="en">
<head>
<meta charset="utf-8">
<title>PactBloom Dashboard</title>
<link href="https://fonts.googleapis.com/css2?family=Source+Sans+3:wght@400;600;700&display=swap" rel="stylesheet">
<style>
:root{
  --green:#3da55d;
  --green-dark:#34914f;
  --black:#0b0b0b;
  --panel:#ffffff;
  --panel-soft:rgba(255,255,255,.93);
  --line:#dfe2e5;
  --title:#4b5b6e;
  --text:#333a40;
  --muted:#7d858c;
  --red:#f0485e;
  --orange:#f7941d;
  --blue:#2f77c4;
  --navy:#1d3f7a;
  --tab-grey:#ececec;
  --icon-grey:#c4c7ca;
}
*{box-sizing:border-box;margin:0;padding:0}
html,body{width:1200px;height:603px;overflow:hidden}
body{font-family:"Source Sans 3",Arial,sans-serif;color:var(--text);position:relative;background:#eef0f1}
.backdrop{position:absolute;inset:59px 0 0 0;background:radial-gradient(ellipse at 50% 60%,#d3d6d8 0%,#e7e9ea 45%,#f4f5f5 100%)}
/* header */
.topbar{position:absolute;left:0;top:0;width:1200px;height:59px;background:var(--green);color:#fff;font-size:12.5px}
.brand{position:absolute;left:0;top:0;width:196px;height:59px;background:var(--black);display:flex;align-items:center;padding-left:22px;gap:9px}
.brand-dot{width:26px;height:26px;border-radius:50%;background:var(--green)}
.brand-name{font-size:17px;font-weight:600;letter-spacing:.5px;color:#fff}
.topbar .abs{position:absolute;display:flex;align-items:center;gap:6px}
.search{position:absolute;left:513px;top:11px;width:407px;height:35px;background:var(--green-dark);border:1px solid #4bb36a;border-radius:2px;display:flex;align-items:center;padding:0 10px;font-size:12px}
.search .ph{color:#a6dbb5;flex:1}
.search .scope{color:#246b39;font-style:italic;margin-right:22px}
.search .saved{color:#fff;font-style:italic;font-weight:600}
.caret{display:inline-block;border:5px solid transparent;border-top:6px solid #246b39;margin:5px 0 0 4px;vertical-align:middle}
.caret.light{border-top-color:#a6dbb5}
.badge{position:absolute;left:1001px;top:13px;background:#f4d21f;color:#333;font-size:8px;font-weight:700;border-radius:7px;padding:0 3px;line-height:11px}
.avatar{position:absolute;left:1079px;top:11px;width:37px;height:37px;border-radius:50%;background:#dcdcdc;border:2px solid #fff}
/* panels */
.panel{position:absolute;background:var(--panel-soft);border:1px solid var(--line)}
.panel-title{height:41px;border-bottom:1px solid var(--line);font-size:19px;font-weight:600;color:var(--title);padding:9px 13px}
/* documents */
.documents{left:20px;top:80px;width:436px;height:279px}
.doc-tabs{position:absolute;left:0;top:41px;width:77px;bottom:0}
.doc-tab{height:58px;background:var(--tab-grey);border-bottom:1px solid #dcdcdc;text-align:center;font-size:10.5px;font-weight:600;color:var(--muted);padding-top:11px}
.doc-tab svg{display:block;margin:0 auto 3px}
.doc-tab.active{background:#fff;color:var(--text);font-size:11.5px}
.doc-list{position:absolute;left:77px;top:41px;right:0;bottom:0;border-left:1px solid var(--line);background:#fff}
.doc-item{position:absolute;left:0;right:14px;height:56px;padding-left:42px}
.doc-item .dot{position:absolute;left:19px;top:20px;width:8px;height:8px;border-radius:50%}
.doc-item h3{font-size:14px;font-weight:400;color:var(--text);white-space:nowrap;overflow:hidden}
.doc-item p{font-size:10px;font-weight:600;color:var(--muted);margin-top:1px}
.x{display:inline-block;width:10px;height:10px;border-radius:50%;background:var(--icon-grey);position:relative;vertical-align:middle;margin-left:8px}
.x::before,.x::after{content:"";position:absolute;left:2px;top:4.5px;width:6px;height:1px;background:#fff;transform:rotate(45deg)}
.x::after{transform:rotate(-45deg)}
.scroll{position:absolute;width:4px;border-radius:2px;background:#cfd2d5}
/* meetings */
.meetings{left:475px;top:80px;width:396px;height:279px}
.meeting{position:absolute;left:14px;right:14px;height:62px}
.m-time{position:absolute;left:0;top:0;width:110px;text-align:center}
.m-time .clock{font-size:19px;color:#4a4f55}
.m-time .clock small{font-size:11px}
.m-time .date{font-size:11px;font-weight:600;color:#333;border-top:1px solid var(--line);margin-top:3px;padding-top:3px}
.m-info{position:absolute;left:120px;top:2px;width:176px;border-left:1px solid var(--line);padding-left:12px;height:50px}
.m-info h4{font-size:14px;font-weight:700;color:var(--navy);white-space:nowrap}
.m-info p{font-size:9.5px;color:#555;line-height:12px}
.m-place{position:absolute;left:298px;top:2px;width:58px;border-left:1px solid var(--line);text-align:center;font-size:10.5px;font-weight:700;color:#333;height:50px}
.m-place svg{display:block;margin:4px auto 2px}
.m-cup{position:absolute;left:8px;top:6px}
/* reminders */
.reminders{left:889px;top:80px;width:291px;height:430px;background:#fff}
.rem-tabs{display:flex;height:47px}
.rem-tab{flex:1;font-size:19px;font-weight:600;color:var(--title);padding:9px 0 0 25px;background:#fff;border-right:1px solid var(--line)}
.rem-tab.off{background:#f0f0f0;color:#b5b9bd;border-bottom:1px solid var(--line)}
.rem{position:absolute;left:13px;right:13px;height:60px;border-bottom:1px solid var(--line)}
.rem-date{position:absolute;left:0;top:5px;width:137px;font-size:11.5px;color:#333}
.rem-date .d{font-size:19px}
.rem-date .ev{display:block;font-size:12px;margin-top:2px}
.rem-date svg{vertical-align:-1px;margin-right:4px}
.rem-note{position:absolute;left:137px;top:3px;width:111px;height:49px;border-left:1px solid var(--line);padding-left:11px;font-size:9.5px;line-height:12.5px;color:#333}
.rem .x{position:absolute;right:0;top:24px;margin:0}
.see-more{position:absolute;left:0;right:0;top:403px;text-align:center;font-size:11.5px;color:#333}
/* footer */
.legal{left:889px;top:527px;width:291px;height:55px;background:#e9eaeb;border:1px solid #d8dadc}
.seal{position:absolute;left:27px;top:11px;width:56px;height:28px;border-radius:4px;background:#fafafa;border:1px solid #cfcfcf}
.seal::before{content:"";position:absolute;left:3px;top:4px;width:19px;height:19px;border-radius:50%;background:#f7c600}
.legal p{position:absolute;left:114px;font-size:10px;color:#8a9096}
/* my latest */
.latest{left:20px;top:378px;width:850px;height:204px;background:#fff}
.latest-head{height:43px;border-bottom:1px solid var(--line);position:relative}
.latest-head h2{position:absolute;left:10px;top:9px;font-size:19px;font-weight:600;color:var(--title)}
.latest-head .when{position:absolute;left:108px;top:6px;border-left:1px solid var(--line);padding-left:13px;font-size:20px;color:#333}
.latest-head .when small{font-size:13px;color:#666}
.today{position:absolute;left:661px;top:15px;font-size:12.5px;color:var(--green);font-weight:600}
.date-search{position:absolute;left:705px;top:8px;width:108px;height:28px;border:1px solid #d5d7d9;font-size:12px;font-style:italic;color:#666;padding:5px 0 0 18px}
.go{position:absolute;left:812px;top:8px;width:30px;height:28px;background:#e6e7e8;border:1px solid #cfd1d3;font-size:12px;text-align:center;padding-top:5px}
.cell{position:absolute;top:43px;height:160px;border-right:1px solid var(--line)}
.cell h5{position:absolute;left:0;right:0;top:12px;text-align:center;font-size:14px;font-weight:400;color:#333}
.cell .foot{position:absolute;left:12px;right:12px;bottom:7px;font-size:12px;font-weight:700}
.usage{left:0;width:206px}
.visits{left:206px;width:211px}
.summary{left:417px;width:432px;border-right:none}
.sum-row{position:absolute;left:18px;width:155px;font-size:12.5px;color:#555;display:flex;align-items:center}
.sum-row .rule{flex:1;height:1px;background:var(--line);margin:0 6px}
.sum-row b{font-size:16px;width:36px}
.arrow{position:absolute;width:12px;height:12px;border-radius:50%}
</style>
</head>
<body>
<div class="backdrop" role="img" aria-label="Soft blurred winter backdrop in pale greys"></div>

<header class="topbar">
  <div class="brand"><span class="brand-dot"></span><span class="brand-name">PACTBLOOM</span></div>
  <div class="abs" style="left:210px;top:21px">
    <svg width="17" height="17" viewBox="0 0 17 17"><circle cx="8.5" cy="8.5" r="8.5" fill="#fff"/><path d="M8.5 4v9M4 8.5h9" stroke="var(--green)" stroke-width="2.2"/></svg>
  </div>
  <div class="abs" style="left:314px;top:21px;font-weight:600">
    <svg width="13" height="14" viewBox="0 0 13 14"><path d="M6.5 1a4 4 0 0 1 4 4v4l1.5 2H1l1.5-2V5a4 4 0 0 1 4-4z" fill="none" stroke="#fff" stroke-width="1.4"/><path d="M5 12.5a1.5 1.5 0 0 0 3 0" stroke="#fff" fill="none" stroke-width="1.2"/></svg>
    <span>Lorem ipsum dolor</span><span style="opacity:.6">|</span><span style="font-weight:700">05.00 min</span>
  </div>
  <div class="search">
    <span class="ph">Search</span>
    <span class="scope">Contracts<i class="caret"></i></span>
    <span class="saved">Saved Search<i class="caret light" style="border-top-color:#a6dbb5"></i></span>
  </div>
  <div class="abs" style="left:948px;top:20px">
    <svg width="19" height="19" viewBox="0 0 20 20"><path fill="#fff" d="M8.5 0h3l.5 2.6 2 .9 2.2-1.5 2.1 2.1-1.5 2.2.9 2 2.6.5v3l-2.6.5-.9 2 1.5 2.2-2.1 2.1-2.2-1.5-2 .9-.5 2.6h-3l-.5-2.6-2-.9-2.2 1.5-2.1-2.1 1.5-2.2-.9-2L0 11.5v-3l2.6-.5.9-2L2 3.8l2.1-2.1L6.3 3.2l2-.9z"/><circle cx="10" cy="10" r="3.3" fill="var(--green)"/></svg>
  </div>
  <div class="abs" style="left:976px;top:20px">
    <svg width="22" height="19" viewBox="0 0 22 19"><path d="M11 1C5.5 1 1 4.5 1 8.5c0 2.2 1.3 4.1 3.4 5.5L3.5 18l4.6-2.6c.9.2 1.9.3 2.9.3 5.5 0 10-3.5 10-7.7S16.5 1 11 1z" fill="#fff"/><circle cx="6.5" cy="8.5" r="1.3" fill="var(--green)"/><circle cx="11" cy="8.5" r="1.3" fill="var(--green)"/><circle cx="15.5" cy="8.5" r="1.3" fill="var(--green)"/></svg>
  </div>
  <span class="badge">23</span>
  <div class="abs" style="left:1012px;top:21px;font-weight:600">Hi,&nbsp; <span style="font-weight:400">Vantyx</span></div>
  <div class="avatar"></div>
  <div class="abs" style="left:1127px;top:21px">
    <svg width="10" height="12" viewBox="0 0 10 12"><rect x="0" y="5" width="10" height="7" rx="1" fill="#fff"/><path d="M2.5 5V3.5a2.5 2.5 0 0 1 5 0V5" stroke="#fff" stroke-width="1.5" fill="none"/></svg>
    <span>Log Out</span>
  </div>
</header>

<section class="panel documents">
  <h2 class="panel-title">Documents</h2>
  <nav class="doc-tabs">
    <div class="doc-tab active"><svg width="12" height="15" viewBox="0 0 12 15"><rect x="0" y="2" width="12" height="13" rx="1" fill="var(--green)"/><rect x="3" y="0" width="6" height="3" fill="var(--green)"/><path d="M3 7h6M3 9.5h6M3 12h6" stroke="#fff"/></svg>Contracts</div>
    <div class="doc-tab"><svg width="16" height="13" viewBox="0 0 16 13"><path d="M1 12h2V8H1zM5 12h2V6H5zM9 12h2V7H9zM13 12h2V3h-2z" fill="#888"/><path d="M1 6l4-3 4 2 6-4" stroke="#888" fill="none"/></svg>Fin &amp; Adm</div>
    <div class="doc-tab"><svg width="15" height="15" viewBox="0 0 15 15"><circle cx="7.5" cy="7.5" r="6.5" fill="none" stroke="#888" stroke-width="1.5"/><circle cx="7.5" cy="6" r="2.3" fill="#888"/><path d="M3.5 12a4.5 4 0 0 1 8 0" fill="#888"/></svg>HR</div>
    <div class="doc-tab"><svg width="13" height="15" viewBox="0 0 13 15"><rect x=".75" y=".75" width="11.5" height="13.5" rx="1" fill="none" stroke="#888" stroke-width="1.5"/><path d="M3 4.5h7M3 7.5h7M3 10.5h7" stroke="#888"/></svg>Com. Reg</div>
  </nav>
  <div class="doc-list">
    <div class="doc-item" style="top:14px"><span class="dot" style="background:var(--orange)"></span><h3>Lorem ipsum dolor sit amet, dolor sit condesec</h3><p>22th may, 10.30 am, 2016 <span style="font-weight:400">|</span> USA<span class="x"></span></p></div>
    <div class="doc-item" style="top:73px"><span class="dot" style="background:#7ac143"></span><h3>Lorem ipsum dolor sit amet, consectetuer.</h3><p>22th may, 10.30 am, 2016 <span style="font-weight:400">|</span> USA<span class="x"></span></p></div>
    <div class="doc-item" style="top:130px"><span class="dot" style="background:var(--blue)"></span><h3>Lorem ipsum dolor sit amet, dolor sit condesec</h3><p>22th may, 10.30 am, 2016 <span style="font-weight:400">|</span> USA<span class="x"></span></p></div>
    <div class="doc-item" style="top:186px"><span class="dot" style="background:#7ac143"></span><h3>Lorem ipsum dolor sit amet, consectetuer.</h3><p>22th may, 10.30 am, 2016 <span style="font-weight:400">|</span> USA<span class="x"></span></p></div>
    <span class="scroll" style="right:8px;top:141px;height:16px"></span>
  </div>
</section>

<section class="panel meetings">
  <h2 class="panel-title">Meetings</h2>
  <div class="meeting" style="top:63px">
    <svg class="m-cup" width="14" height="12" viewBox="0 0 14 12"><path d="M1 4h9v4a3 3 0 0 1-3 3H4a3 3 0 0 1-3-3z" fill="var(--red)"/><path d="M10 5h1.5a1.5 1.5 0 0 1 0 3H10" stroke="var(--red)" fill="none"/><path d="M4 0v2M7 0v2" stroke="var(--red)"/></svg>
    <div class="m-time"><div class="clock">12.30 <small>pm</small></div><div class="date">25 MAY, 2016</div></div>
    <div class="m-info"><h4>Lorem ipsum dolor sitrem</h4><p>Lorem ipsum dolor sit amet, consec tetuer adipiscing elit.</p></div>
    <div class="m-place"><svg width="16" height="22" viewBox="0 0 16 22"><path d="M8 0a8 8 0 0 1 8 8c0 6-8 14-8 14S0 14 0 8a8 8 0 0 1 8-8z" fill="var(--green)"/><circle cx="8" cy="8" r="3" fill="#fff"/></svg>CANADA</div>
    <span class="x" style="position:absolute;right:-2px;top:4px;margin:0"></span>
  </div>
  <div class="meeting" style="top:134px">
    <svg class="m-cup" width="14" height="12" viewBox="0 0 14 12"><path d="M1 4h9v4a3 3 0 0 1-3 3H4a3 3 0 0 1-3-3z" fill="var(--orange)"/><path d="M10 5h1.5a1.5 1.5 0 0 1 0 3H10" stroke="var(--orange)" fill="none"/><path d="M4 0v2M7 0v2" stroke="var(--orange)"/></svg>
    <div class="m-time"><div class="clock">02.30 <small>pm</small></div><div class="date">26 MAY, 2016</div></div>
    <div class="m-info"><h4>Lorem ipsum dolor</h4><p>Lorem ipsum dolor sit amet, consec tetuer adipiscing elit.</p></div>
    <div class="m-place"><svg width="16" height="22" viewBox="0 0 16 22"><path d="M8 0a8 8 0 0 1 8 8c0 6-8 14-8 14S0 14 0 8a8 8 0 0 1 8-8z" fill="var(--green)"/><circle cx="8" cy="8" r="3" fill="#fff"/></svg>PARIS</div>
    <span class="x" style="position:absolute;right:-2px;top:4px;margin:0"></span>
  </div>
  <div class="meeting" style="top:208px">
    <svg class="m-cup" width="14" height="12" viewBox="0 0 14 12"><path d="M1 4h9v4a3 3 0 0 1-3 3H4a3 3 0 0 1-3-3z" fill="var(--orange)"/><path d="M10 5h1.5a1.5 1.5 0 0 1 0 3H10" stroke="var(--orange)" fill="none"/><path d="M4 0v2M7 0v2" stroke="var(--orange)"/></svg>
    <div class="m-time"><div class="clock">02.30 <small>pm</small></div><div class="date">26 MAY, 2016</div></div>
    <div class="m-info"><h4>Lorem ipsum dolor sitrem</h4><p>Lorem ipsum dolor sit amet, consec tetuer adipiscing elit.</p></div>
    <div class="m-place"><svg width="16" height="22" viewBox="0 0 16 22"><path d="M8 0a8 8 0 0 1 8 8c0 6-8 14-8 14S0 14 0 8a8 8 0 0 1 8-8z" fill="var(--green)"/><circle cx="8" cy="8" r="3" fill="#fff"/></svg>PARIS</div>
    <span class="x" style="position:absolute;right:-2px;top:4px;margin:0"></span>
  </div>
  <span class="scroll" style="right:7px;top:63px;height:18px"></span>
</section>

<section class="panel reminders">
  <div class="rem-tabs"><div class="rem-tab">Reminders</div><div class="rem-tab off">Activity Feed</div></div>
  <div class="rem" style="top:50px"><div class="rem-date"><svg width="13" height="13" viewBox="0 0 13 13"><rect x=".5" y="1.5" width="12" height="11" rx="1" fill="none" stroke="var(--red)"/><rect x=".5" y="1.5" width="12" height="3" fill="var(--red)"/><path d="M3 7h2M6 7h2M9 7h1M3 9.5h2M6 9.5h2" stroke="var(--red)"/></svg><span class="d">25</span> may&nbsp; 05.30 pm<span class="ev">Board Meetng&nbsp; |&nbsp; Canda</span></div><div class="rem-note">Lorem ipsum dolor sit amet, consec tetuer adipiscing elit.</div><span class="x"></span></div>
  <div class="rem" style="top:110px"><div class="rem-date"><svg width="13" height="13" viewBox="0 0 13 13"><rect x=".5" y="1.5" width="12" height="11" rx="1" fill="none" stroke="var(--orange)"/><rect x=".5" y="1.5" width="12" height="3" fill="var(--orange)"/><path d="M3 7h2M6 7h2M9 7h1M3 9.5h2M6 9.5h2" stroke="var(--orange)"/></svg><span class="d">26</span> may&nbsp; 05.30 pm<span class="ev">Board Meetng&nbsp; |&nbsp; Canda</span></div><div class="rem-note">Lorem ipsum dolor sit amet, consec tetuer adipiscing elit.</div><span class="x"></span></div>
  <div class="rem" style="top:170px"><div class="rem-date"><svg width="13" height="13" viewBox="0 0 13 13"><rect x=".5" y="1.5" width="12" height="11" rx="1" fill="none" stroke="var(--orange)"/><rect x=".5" y="1.5" width="12" height="3" fill="var(--orange)"/><path d="M3 7h2M6 7h2M9 7h1M3 9.5h2M6 9.5h2" stroke="var(--orange)"/></svg><span class="d">27</span> may&nbsp; 05.30 pm<span class="ev">Board Meetng&nbsp; |&nbsp; Canda</span></div><div class="rem-note">Lorem ipsum dolor sit amet, consec tetuer adipiscing elit.</div><span class="x"></span></div>
  <div class="rem" style="top:229px"><div class="rem-date"><svg width="13" height="13" viewBox="0 0 13 13"><rect x=".5" y="1.5" width="12" height="11" rx="1" fill="none" stroke="var(--orange)"/><rect x=".5" y="1.5" width="12" height="3" fill="var(--orange)"/><path d="M3 7h2M6 7h2M9 7h1M3 9.5h2M6 9.5h2" stroke="var(--orange)"/></svg><span class="d">28</span> may&nbsp; 05.30 pm<span class="ev">Board Meetng&nbsp; |&nbsp; Canda</span></div><div class="rem-note">Lorem ipsum dolor sit amet, consec tetuer adipiscing elit.</div><span class="x"></span></div>
  <div class="rem" style="top:289px"><div class="rem-date"><svg width="13" height="13" viewBox="0 0 13 13"><rect x=".5" y="1.5" width="12" height="11" rx="1" fill="none" stroke="var(--orange)"/><rect x=".5" y="1.5" width="12" height="3" fill="var(--orange)"/><path d="M3 7h2M6 7h2M9 7h1M3 9.5h2M6 9.5h2" stroke="var(--orange)"/></svg><span class="d">27</span> may&nbsp; 05.30 pm<span class="ev">Board Meetng&nbsp; |&nbsp; Canda</span></div><div class="rem-note">Lorem ipsum dolor sit amet, consec tetuer adipiscing elit.</div><span class="x"></span></div>
  <div class="rem" style="top:349px"><div class="rem-date"><svg width="13" height="13" viewBox="0 0 13 13"><rect x=".5" y="1.5" width="12" height="11" rx="1" fill="none" stroke="var(--orange)"/><rect x=".5" y="1.5" width="12" height="3" fill="var(--orange)"/><path d="M3 7h2M6 7h2M9 7h1M3 9.5h2M6 9.5h2" stroke="var(--orange)"/></svg><span class="d">28</span> may&nbsp; 05.30 pm<span class="ev">Board Meetng&nbsp; |&nbsp; Canda</span></div><div class="rem-note">Lorem ipsum dolor sit amet, consec tetuer adipiscing elit.</div><span class="x"></span></div>
  <div class="see-more">See More</div>
</section>

<footer class="panel legal">
  <div class="seal"></div>
  <p style="top:10px">Copyright © 2016 PactBloom Ltd</p>
  <p style="top:26px">Terms of Use Privacy</p>
</footer>

<section class="panel latest">
  <div class="latest-head">
    <h2>My Latest</h2>
    <div class="when">27 <small>May, 2016</small></div>
    <span class="today">Today</span>
    <div class="date-search">Search by date</div>
    <div class="go">Go</div>
  </div>

  <div class="cell usage">
    <h5>Monthly Usage</h5>
    <svg width="206" height="160" viewBox="0 0 206 160" style="position:absolute;left:0;top:0">
      <path d="M28 128A73 73 0 0 1 174 128L130 128A29 29 0 0 0 72 128Z" fill="#ececec"/>
      <path d="M28 128A73 73 0 0 1 78.4 58.6L92 100.4A29 29 0 0 0 72 128Z" fill="var(--red)"/>
      <line x1="12" y1="128" x2="190" y2="128" stroke="#d6d8da"/>
      <polygon points="82.5,71 97,129 105,127" fill="#222"/>
      <circle cx="101" cy="128" r="6" fill="#222"/>
    </svg>
    <div class="foot"><span style="font-weight:400;color:#333">Total</span><span style="color:var(--orange);margin-left:36px">1,026</span><span style="color:var(--red);float:right">40%</span></div>
  </div>

  <div class="cell visits">
    <span class="arrow" style="left:16px;top:15px;background:#ccc"></span>
    <h5>Visitor per day</h5>
    <span class="arrow" style="right:16px;top:15px;background:var(--orange)"></span>
    <svg width="211" height="160" viewBox="0 0 211 160" style="position:absolute;left:0;top:0;font-family:inherit">
      <g stroke="#dadcde"><line x1="48" y1="48" x2="180" y2="48"/><line x1="48" y1="74" x2="180" y2="74"/><line x1="48" y1="99" x2="180" y2="99"/></g>
      <g font-size="9" fill="#333" text-anchor="end"><text x="38" y="51">100%</text><text x="38" y="77">50%</text><text x="38" y="102">0%</text></g>
      <path d="M53 98L76 74L92 85L116 60L140 84L154 69V99H53Z" fill="#fbe3d3" opacity=".7"/>
      <polyline points="53,98 76,74 92,85 116,60 140,84 154,69" fill="none" stroke="#7ac143" stroke-width="3"/>
      <g fill="#fff" stroke="var(--red)" stroke-width="2"><circle cx="76" cy="74" r="5"/><circle cx="116" cy="60" r="5"/><circle cx="154" cy="69" r="5"/></g>
      <g font-size="9" fill="#333" text-anchor="middle"><text x="23" y="120" fill="var(--green)" font-weight="700">May</text><text x="52" y="120">0</text><text x="76" y="120">5</text><text x="101" y="120">10</text><text x="127" y="120">15</text><text x="152" y="120">20</text></g>
      <line x1="10" y1="131" x2="200" y2="131" stroke="#d6d8da"/>
    </svg>
    <div class="foot"><span style="color:var(--orange)">1,026</span><span style="color:var(--blue);float:right">↑ 10%</span></div>
  </div>

  <div class="cell summary">
    <h5>Last Month Summery</h5>
    <span class="scroll" style="right:8px;top:14px;height:16px"></span>
    <div class="sum-row" style="top:44px"><span>Contracts</span><span class="rule"></span><b style="color:var(--red)">66 %</b></div>
    <div class="sum-row" style="top:69px"><span>Finance &amp; Admin</span><span class="rule"></span><b style="color:#5aa83a">47 %</b></div>
    <div class="sum-row" style="top:93px"><span>HR</span><span class="rule"></span><b style="color:var(--orange)">5 %</b></div>
    <span style="position:absolute;left:191px;top:45px;font-size:12.5px;color:#555">Remainder</span>
    <svg width="60" height="34" viewBox="0 0 60 34" style="position:absolute;left:192px;top:64px">
      <path d="M1 30A29 29 0 0 1 59 30L47 30A17 17 0 0 0 13 30Z" fill="#ececec"/>
      <path d="M1 30A29 29 0 0 1 21 2.4L24.7 13.8A17 17 0 0 0 13 30Z" fill="var(--red)"/>
      <line x1="27" y1="15" x2="30" y2="30" stroke="#222" stroke-width="2"/>
    </svg>
    <span style="position:absolute;left:210px;top:100px;font-size:12px;font-weight:700">40%</span>
    <span style="position:absolute;left:321px;top:45px;font-size:12.5px;color:#555">Daily activity</span>
    <span class="arrow" style="left:282px;top:86px;background:#ccc"></span>
    <span class="arrow" style="left:396px;top:86px;background:var(--orange)"></span>
    <svg width="96" height="50" viewBox="0 0 96 50" style="position:absolute;left:296px;top:64px">
      <g fill="#e6e7e8"><rect x="0" y="0" width="10" height="34"/><rect x="16" y="0" width="10" height="34"/><rect x="32" y="0" width="10" height="34"/><rect x="48" y="0" width="10" height="34"/><rect x="64" y="0" width="10" height="34"/><rect x="80" y="0" width="10" height="34"/></g>
      <g fill="#7ac143"><rect x="0" y="18" width="10" height="16"/><rect x="16" y="13" width="10" height="21"/><rect x="32" y="21" width="10" height="13"/><rect x="48" y="18" width="10" height="16"/><rect x="64" y="13" width="10" height="21"/><rect x="80" y="24" width="10" height="10"/></g>
      <g font-size="8" font-weight="700" fill="#333" text-anchor="middle"><text x="5" y="46">1</text><text x="21" y="46">2</text><text x="37" y="46">3</text><text x="53" y="46">4</text><text x="69" y="46">5</text><text x="85" y="46">6</text></g>
    </svg>
    <span style="position:absolute;left:16px;right:16px;top:131px;height:1px;background:#d6d8da"></span>
    <div class="foot" style="left:18px"><span style="font-weight:400;color:#333">Total</span><span style="color:var(--orange);margin-left:10px">22,026</span><span style="color:var(--blue);float:right">↑ 22%</span></div>
  </div>
</section>
</body>
</html>
```